Environmental Plastics Infographic

We need a series of infographics that can be used individually or as a combined presentation. We'd like the combined piece to include an introduction and conclusion along with 4-5 infographics. Each infographic (information unit) should also work as a standalone. We are trying to help people visualize size proportions and ratios to put carbon footprint/life cycle data for EPS foam packaging in perspective. We are looking for something creative to help people understand what the figures represent in terms they are familiar with.
To view our typical company design/style please see our website at www.trellamark.org. Our primary RGB colors are: (187,140,9); (94,47,29); (94,138,164); and (164,167,15). Secondary RGB colors are (249,162,28) and (218,210,208). Our title/header font is DIN Next LT Pro and our copy font is Calibri 10.5 pt. We can deviate from the font specification if beneficial and welcome interesting text treatments and typography.
We want sufficient white space with easy to grasp message concept with visual components. The attachment showing data points present concepts on how to show the data impacts but are only representative of a baseline concept - we are confident a professional designer can do a much better job with better visual presentation.
Target Market(s)
The audience is international brand manufacturers (brightmoor, kavo), US legislators & government agencies.
Nice to have
- Other creative ideas on how to present this messaging is encouraged.

```html
<!DOCTYPE html>
<html lang="en">
<head>
<meta charset="utf-8">
<title>EPS Life Cycle Infographic Series</title>
<link href="https://fonts.googleapis.com/css2?family=Rubik:wght@500;700&family=Roboto:ital,wght@0,400;0,500;1,400;1,500&display=swap" rel="stylesheet">
<style>
:root{
  --gold:#b98a0c;
  --green:#10a05a;
  --green-soft:#3db877;
  --text:#3a3a3a;
  --muted:#555;
  --faint:#e6e9ee;
  --red:#e0261d;
  --rule:#d9822b;
  --sky:#e9f1f8;
  --pool:#2f7fe0;
  --pool-deep:#1f6fd6;
  --car:#e8532a;
  --white:#fff;
}
*{box-sizing:border-box;margin:0;padding:0}
html,body{width:1200px;height:1000px;overflow:hidden;background:var(--white)}
.canvas{position:relative;width:1200px;height:1000px;overflow:hidden;font-family:"Roboto",Arial,sans-serif;color:var(--text)}
.abs{position:absolute}
.heading{font-family:"Rubik",Arial,sans-serif;font-weight:700;color:var(--gold);font-size:22.5px;text-align:center;white-space:nowrap}
.heading--who{font-size:27px}
.title{font-family:"Rubik",Arial,sans-serif;font-weight:500;color:var(--green);font-size:26.5px;text-align:center;white-space:nowrap}
.lead{font-style:italic;font-size:14px;color:var(--text);line-height:20px;white-space:nowrap}
.lead .amp{font-family:"Rubik",Arial,sans-serif;font-style:normal;font-weight:700;font-size:26px;color:var(--faint);position:absolute;left:-30px;top:-4px}
.body{font-size:10px;line-height:17.5px;color:var(--muted);text-align:center}
.caption{font-style:italic;font-weight:500;font-size:12px;line-height:18px;text-align:center;color:var(--text)}
.number{font-family:"Rubik",Arial,sans-serif;font-weight:700;font-style:italic;font-size:28px;color:#f1f3f6}
.badge{width:46px;height:46px}
.pool{
  border-radius:150px 0 0 0;
  background:
    linear-gradient(180deg,transparent 0 93%,var(--white) 93% 95%,var(--pool) 95% 100%),
    radial-gradient(ellipse 70% 30% at 60% 72%,#7fb6f2 0%,transparent 70%),
    linear-gradient(180deg,#eaf3fd 0%,#cfe3f8 38%,#ffffff 54%,#f4f8fc 58%,#5aa0ec 62%,#3c8ae6 76%,var(--pool-deep) 90%,#ffffff 92%);
}
.foam{border-radius:6px;background:radial-gradient(ellipse at 50% 55%,#ffffff 0%,#f1f3f5 55%,#ffffff 100%)}
.carton{border-radius:4px;background:linear-gradient(180deg,#ffffff 0%,#d2ac78 12%,#c49560 45%,#b5844f 70%,#a57747 100%)}
.scene{
  background:
    linear-gradient(180deg,transparent 0 82%,rgba(255,255,255,.95) 100%),
    radial-gradient(ellipse 36% 24% at 45% 63%,var(--car) 0%,#ef6a3a 45%,rgba(239,106,58,0) 100%),
    radial-gradient(ellipse 30% 20% at 12% 55%,#ffffff 0%,rgba(255,255,255,0) 100%),
    linear-gradient(180deg,#ffffff 0%,var(--sky) 18%,#dde6ee 50%,#e8edf2 75%,#f6f8fa 100%);
}
.icons{display:flex;gap:19px}
.timeline{height:1px;background:var(--rule)}
.dot{width:7px;height:7px;border-radius:50%;background:var(--red);top:-3px}
.km{font-size:9px;font-style:italic;color:var(--red);text-align:center;width:80px}
.co2{font-size:12px;font-weight:500;color:#333;text-align:center;width:100px}
.brand{display:flex;align-items:center;gap:8px}
.brand .mark{width:44px;height:44px;border-radius:50%;background:var(--gold)}
.brand .name{font-family:"Roboto",Arial,sans-serif;font-size:10px;line-height:12px;color:#5e2f1d;font-weight:500}
.products{background:linear-gradient(90deg,#ffffff 0%,#e3e6ea 12%,#ffffff 30%,#ffffff 52%,#eceef0 60%,#f7f8f9 75%,#e9ebee 88%,#ffffff 100%)}
</style>
</head>
<body>
<div class="canvas">

  <svg width="0" height="0" style="position:absolute">
    <defs>
      <symbol id="eco-badge" viewBox="0 0 46 46">
        <path d="M23 4 C19 8 19 12 23 15 C27 12 27 8 23 4Z" fill="#3db877"/>
        <path d="M14 8 C15 13 18 15 22 15 C21 11 18 9 14 8Z" fill="#3db877"/>
        <path d="M32 8 C31 13 28 15 24 15 C25 11 28 9 32 8Z" fill="#3db877"/>
        <ellipse cx="36" cy="33" rx="9" ry="5" fill="#eef1f4"/>
        <circle cx="23" cy="30" r="13" fill="#10a05a"/>
        <circle cx="23" cy="30" r="7" fill="none" stroke="#fff" stroke-width="2"/>
      </symbol>
      <symbol id="pin" viewBox="0 0 30 32">
        <circle cx="15" cy="14" r="13" fill="#fff" stroke="#e0261d" stroke-width="2"/>
        <path d="M11 27 L15 31 L19 27Z" fill="#e0261d"/>
        <circle cx="15" cy="14" r="7" fill="#e0261d"/>
      </symbol>
    </defs>
  </svg>

  <!-- Column 1 : water consumption -->
  <section class="column column--water">
    <div class="abs heading" style="left:50px;width:355px;top:24px">Manufacturing 1 ton of EPS</div>
    <p class="abs lead" style="left:135px;top:59px"><span class="amp">&amp;</span>it’s equivalent of consuming 300 hours of<br>light for a single lightbulb.</p>
    <svg class="abs badge" style="left:204px;top:118px" role="img" aria-label="Recycling leaf badge"><use href="#eco-badge"/></svg>
    <div class="abs title" style="left:50px;width:355px;top:185px">EPS Life Cycle</div>
    <p class="abs lead" style="left:144px;top:222px"><span class="amp">&amp;</span>our efficient water consumption</p>
    <div class="abs pool" style="left:50px;top:252px;width:355px;height:193px" role="img" aria-label="Illustration of a backyard swimming pool with parasols, loungers and potted palms"></div>
    <p class="abs caption" style="left:50px;width:355px;top:458px;font-weight:400">24,000 gallons | 40x20 foot swimming pool<br><b style="font-weight:500">(avg 4 ft depth)</b></p>
    <div class="abs heading" style="left:50px;width:355px;top:510px">Manufacturing 1 ton of EPS</div>
    <p class="abs lead" style="left:129px;top:545px"><span class="amp">&amp;</span>it requires only of xx swimming pools.</p>
    <div class="abs foam" style="left:62px;top:612px;width:165px;height:100px" role="img" aria-label="Stack of white EPS foam containers"></div>
    <div class="abs carton" style="left:247px;top:588px;width:128px;height:128px" role="img" aria-label="Stack of corrugated cardboard boxes"></div>
    <p class="abs caption" style="left:62px;width:165px;top:740px">1 ton of EPS uses xxx<br>gallons of water</p>
    <p class="abs caption" style="left:235px;width:165px;top:740px">1 ton of Corrugated paper<br>uses xxx gallons of water</p>
  </section>

  <!-- Column 2 : global warming -->
  <section class="column column--warming">
    <div class="abs heading heading--who" style="left:430px;width:355px;top:10px">Who We Are?</div>
    <p class="abs body" style="left:430px;width:355px;top:48px">EPS is a product that provides smart solutions and durable,<br>efficient results. Equally important, EPS is a sustainable<br>product that is recyclable and environmentally sound.</p>
    <span class="abs number" style="left:675px;top:142px">#2</span>
    <svg class="abs badge" style="left:584px;top:122px" role="img" aria-label="Recycling leaf badge"><use href="#eco-badge"/></svg>
    <div class="abs title" style="left:430px;width:355px;top:190px">EPS Life Cycle</div>
    <p class="abs lead" style="left:514px;top:227px"><span class="amp">&amp;</span>very low impact on global warming</p>
    <div class="abs scene" style="left:430px;top:252px;width:355px;height:318px" role="img" aria-label="Red hatchback car driving through exhaust clouds in front of a pale city skyline"></div>
    <div class="abs icons" style="left:490px;top:270px">
      <svg width="30" height="32" role="img" aria-label="CO2 icon"><use href="#pin"/></svg>
      <svg width="30" height="32" role="img" aria-label="Globe icon"><use href="#pin"/></svg>
      <svg width="30" height="32" role="img" aria-label="Resource icon"><use href="#pin"/></svg>
      <svg width="30" height="32" role="img" aria-label="Acid rain icon"><use href="#pin"/></svg>
      <svg width="30" height="32" role="img" aria-label="Lungs icon"><use href="#pin"/></svg>
    </div>
    <div class="abs timeline" style="left:460px;top:591px;width:295px">
      <span class="abs dot" style="left:44px"></span><span class="abs dot" style="left:142px"></span><span class="abs dot" style="left:242px"></span>
    </div>
    <span class="abs km" style="left:467px;top:600px">1 km</span>
    <span class="abs km" style="left:565px;top:600px">50 km</span>
    <span class="abs km" style="left:665px;top:600px">100 km</span>
    <span class="abs co2" style="left:457px;top:614px">115.5 kg CO2</span>
    <span class="abs co2" style="left:555px;top:614px">5,775 kg CO2</span>
    <span class="abs co2" style="left:655px;top:614px">11,550 kg CO2</span>
    <div class="abs heading" style="left:430px;width:355px;top:650px">Manufacturing 1 ton of EPS</div>
    <p class="abs lead" style="left:494px;top:684px"><span class="amp">&amp;</span>it’s equivalent of driving your car 31 miles</p>
    <p class="abs body" style="left:430px;width:355px;top:717px">EPS has a very low global warming impact compared to other<br>packaging materials. The carbon footprint for manufacturing<br>1 ton of EPS is&nbsp; the equivalent of driving your car 31 miles.</p>
    <span class="abs number" style="left:508px;top:796px">#3</span>
    <svg class="abs badge" style="left:584px;top:794px" role="img" aria-label="Recycling leaf badge"><use href="#eco-badge"/></svg>
    <div class="abs title" style="left:430px;width:355px;top:862px">EPS Life Cycle</div>
    <p class="abs lead" style="left:512px;top:899px"><span class="amp">&amp;</span>our usage of non-renewable energy</p>
    <div class="abs products" style="left:455px;top:952px;width:300px;height:48px" role="img" aria-label="Lightbulb and clear plastic food containers"></div>
  </section>

  <!-- Column 3 : combined intro -->
  <section class="column column--intro">
    <div class="abs brand" style="left:950px;top:233px">
      <span class="mark"></span>
      <span class="name">Trellamark<br>Alliance</span>
    </div>
    <span class="abs number" style="left:860px;top:270px">#1</span>
    <div class="abs heading heading--who" style="left:810px;width:355px;top:309px">Who We Are?</div>
    <p class="abs body" style="left:810px;width:355px;top:348px">EPS is a product that provides smart solutions and durable,<br>efficient results. Equally important, EPS is a sustainable<br>product that is recyclable and environmentally sound.</p>
    <span class="abs number" style="left:1055px;top:442px">#2</span>
    <svg class="abs badge" style="left:964px;top:422px" role="img" aria-label="Recycling leaf badge"><use href="#eco-badge"/></svg>
    <div class="abs title" style="left:810px;width:355px;top:489px">EPS Life Cycle</div>
    <p class="abs lead" style="left:894px;top:526px"><span class="amp">&amp;</span>very low impact on global warming</p>
    <div class="abs scene" style="left:810px;top:552px;width:355px;height:318px" role="img" aria-label="Red hatchback car driving through exhaust clouds in front of a pale city skyline"></div>
    <div class="abs icons" style="left:870px;top:569px">
      <svg width="30" height="32" role="img" aria-label="CO2 icon"><use href="#pin"/></svg>
      <svg width="30" height="32" role="img" aria-label="Globe icon"><use href="#pin"/></svg>
      <svg width="30" height="32" role="img" aria-label="Resource icon"><use href="#pin"/></svg>
      <svg width="30" height="32" role="img" aria-label="Acid rain icon"><use href="#pin"/></svg>
      <svg width="30" height="32" role="img" aria-label="Lungs icon"><use href="#pin"/></svg>
    </div>
    <div class="abs timeline" style="left:840px;top:890px;width:295px">
      <span class="abs dot" style="left:44px"></span><span class="abs dot" style="left:142px"></span><span class="abs dot" style="left:242px"></span>
    </div>
    <span class="abs km" style="left:847px;top:899px">1 km</span>
    <span class="abs km" style="left:945px;top:899px">50 km</span>
    <span class="abs km" style="left:1045px;top:899px">100 km</span>
    <span class="abs co2" style="left:837px;top:913px">115.5 kg CO2</span>
    <span class="abs co2" style="left:935px;top:913px">5,775 kg CO2</span>
    <span class="abs co2" style="left:1035px;top:913px">11,550 kg CO2</span>
    <div class="abs heading" style="left:810px;width:355px;top:949px">Manufacturing 1 ton of EPS</div>
    <p class="abs lead" style="left:874px;top:981px"><span class="amp">&amp;</span>it’s equivalent of driving your car 31 miles</p>
  </section>

</div>
</body>
</html>
```